Mellow Truffles. We need a website as delcious as our chocolate.

I need a website to promote our humble chocolate business. We our proud of are chocolate because we use only our favorite ingredients. We believe in originality and complete enjoyment of our chocolates. I am looking for a sleek and smooth website. I would like to see typical pages such as contact information and an intro. I would like to have a product page, which can be easily updated with photos of new chocolate. I would also like to see a page where we can educate customers about chocolate. This might be tricky but I would like our customers to leave the site knowing they are getting great chocolate! I have a logo and general color scheme, which I will try to upload somewhere. I looking for an original and exciting website.
Updates

Websites we like:

1. http://www.paul-van-orlen.example/ (looks really good)

2. http://www.tremilcocoa.example/

uploaded logo !

Target Market(s)

People who enjoy chocolate.

Industry/Entity Type

Business

Requirements
Must have
• User Friendly
Page were pictures of new chocolate can be easily updated.

Nice to have
• Calming and appetizing music
Section where recent tweets can show up on the site.

```html
<!DOCTYPE html>
<html lang="en">
<head>
<meta charset="utf-8">
<title>Mellow Truffles – Homemade with Passion</title>
<link href="https://fonts.googleapis.com/css2?family=Source+Sans+3:wght@400;600&family=Pinyon+Script&family=Dancing+Script:wght@600&display=swap" rel="stylesheet">
<style>
  :root {
    --page-pink: #efc9ea;
    --page-pink-deep: #e6b3df;
    --tab-top: #c56bc0;
    --tab-bottom: #a9469f;
    --plum: #a21e8c;
    --panel-purple: #c15ebf;
    --panel-edge: #9c3b98;
    --cocoa: #4b2218;
    --cocoa-mid: #6d433a;
    --cocoa-dark: #4a2b25;
    --white: #ffffff;
    --grey-box: #d9d9d9;
    --grey-dark: #4d4d4d;
  }
  * { box-sizing: border-box; margin: 0; padding: 0; }
  html, body { width: 1200px; height: 697px; overflow: hidden; }
  body {
    position: relative;
    font-family: "Source Sans 3", Arial, sans-serif;
    background: radial-gradient(ellipse at 50% 40%, var(--page-pink) 0%, var(--page-pink-deep) 100%);
  }
  .site { position: absolute; left: 161px; top: 0; width: 873px; height: 697px; }

  .brand { position: absolute; left: 14px; top: 20px; color: var(--cocoa); }
  .brand-name { font-size: 34px; font-weight: 600; line-height: 1; letter-spacing: .5px; }
  .brand-tagline { font-size: 15px; font-weight: 400; margin-top: 6px; color: #7b2d4f; }

  .main-nav { position: absolute; left: 296px; top: 61px; display: flex; gap: 1px; }
  .nav-tab {
    width: 113px; height: 60px; border-radius: 56px 56px 0 0;
    background: linear-gradient(var(--tab-top), var(--tab-bottom));
    position: relative; text-align: center;
    color: var(--white); text-decoration: none;
  }
  .nav-icon {
    position: absolute; left: 38px; top: 6px; width: 38px; height: 28px;
    border-radius: 50%; background: #7a3b22;
  }
  .nav-icon.note { background: #f3d48e; border-radius: 4px; width: 28px; left: 43px; }
  .nav-icon.cookie { background: #c97a35; }
  .nav-icon.cup { background: #efe3d5; }
  .nav-label {
    position: absolute; left: 0; right: 0; bottom: 1px;
    font-family: "Dancing Script", cursive; font-size: 19px; font-weight: 600;
  }

  .content { position: absolute; left: 0; top: 121px; width: 873px; height: 473px; background: var(--white); }

  .hero {
    position: absolute; left: 14px; top: 13px; width: 614px; height: 436px;
    background: linear-gradient(160deg, #e9e4e6 0%, #b5a8a6 30%, #6a3a2b 55%, #e7a9d2 80%, #d3c6c9 100%);
  }
  .hero-caption {
    position: absolute; left: 208px; top: 62px; width: 404px; height: 96px;
    background: rgba(255,255,255,.82); text-align: right; padding: 6px 12px 0 0;
  }
  .hero-kicker { font-family: "Pinyon Script", cursive; font-size: 38px; color: var(--cocoa); line-height: 1.05; }
  .hero-title { font-size: 31px; color: var(--plum); line-height: 1.2; }

  .discount {
    position: absolute; left: 640px; top: 13px; width: 213px; height: 77px;
    border: 1px solid var(--grey-dark);
    background: linear-gradient(#f4f4f4, var(--grey-box));
  }
  .discount-value { position: absolute; left: 5px; top: 2px; color: var(--cocoa); font-weight: 600; line-height: .95; }
  .discount-value .pct { font-size: 38px; display: block; }
  .discount-value .off { font-size: 32px; display: block; padding-left: 24px; }
  .discount-head {
    position: absolute; left: 88px; top: 7px; font-size: 13px; line-height: 16px;
    color: var(--plum); font-weight: 600; white-space: nowrap;
  }
  .discount-text { position: absolute; left: 89px; top: 25px; width: 120px; font-size: 11px; line-height: 14px; color: #333; }
  .discount-cta {
    position: absolute; left: 124px; top: 54px; width: 80px; height: 18px;
    background: var(--grey-dark); color: var(--white); font-size: 12px; padding-left: 4px; line-height: 18px;
  }

  .feature {
    position: absolute; left: 644px; top: 101px; width: 215px; height: 222px;
    background: var(--panel-purple); border: 2px solid var(--panel-edge);
    color: var(--white); padding: 6px 8px;
  }
  .feature-title { font-size: 26px; font-weight: 400; line-height: 1.1; margin-bottom: 8px; white-space: nowrap; letter-spacing: -.2px; }
  .feature p { font-size: 11px; line-height: 14px; margin-bottom: 12px; }
  .feature-more { position: absolute; right: 10px; bottom: 8px; font-size: 13px; line-height: 16px; }

  .promo {
    position: absolute; left: 649px; top: 334px; width: 213px; height: 115px;
    border: 1px solid #c9a4cf;
    background: linear-gradient(120deg, #f4eef6 0%, #e2d1e8 50%, #5a3a2b 100%);
  }
  .promo-line { position: absolute; right: 8px; top: 8px; font-size: 10px; line-height: 12px; color: #333; font-weight: 600; white-space: nowrap; }
  .promo-name { position: absolute; left: 8px; top: 28px; font-size: 20px; line-height: 24px; font-weight: 600; color: var(--cocoa); white-space: nowrap; }
  .promo-foot { position: absolute; left: 6px; bottom: 4px; font-size: 9px; color: var(--cocoa); font-weight: 600; }

  .site-footer {
    position: absolute; left: 0; top: 594px; width: 873px; height: 103px;
    background: linear-gradient(var(--cocoa-mid), var(--cocoa-dark)); color: var(--white);
  }
  .footer-nav { position: absolute; left: 29px; top: 12px; font-size: 12px; font-weight: 600; display: flex; }
  .footer-nav span.sep { margin: 0 36px 0 34px; }
  .copyright { position: absolute; left: 28px; top: 37px; font-size: 13px; font-weight: 600; }
  .follow { position: absolute; left: 36px; top: 70px; font-size: 14px; font-weight: 600; display: flex; align-items: center; gap: 10px; }
  .social { font-size: 11px; font-weight: 600; display: flex; align-items: center; gap: 4px; }
  .social i { display: inline-block; width: 10px; height: 10px; background: #e9b54a; border-radius: 2px; }
  .payments { position: absolute; left: 696px; top: 0; }
</style>
</head>
<body>
<div class="site">
  <header>
    <div class="brand">
      <div class="brand-name">Mellow Truffles</div>
      <div class="brand-tagline">homemade with passion</div>
    </div>
    <nav class="main-nav">
      <a class="nav-tab" href="#"><span class="nav-icon" role="img" aria-label="Chocolate bonbons"></span><span class="nav-label">Home</span></a>
      <a class="nav-tab" href="#"><span class="nav-icon note" role="img" aria-label="Note paper"></span><span class="nav-label">Products</span></a>
      <a class="nav-tab" href="#"><span class="nav-icon cookie" role="img" aria-label="Cookies"></span><span class="nav-label">Services</span></a>
      <a class="nav-tab" href="#"><span class="nav-icon" role="img" aria-label="Chocolate pieces"></span><span class="nav-label">Company</span></a>
      <a class="nav-tab" href="#"><span class="nav-icon cup" role="img" aria-label="Coffee cup"></span><span class="nav-label">Cantact</span></a>
    </nav>
  </header>

  <main class="content">
    <section class="hero" role="img" aria-label="Chocolate waffle with strawberry sauce and mint on a plate over a pink napkin">
      <div class="hero-caption">
        <div class="hero-kicker">Dicover a New Way to</div>
        <div class="hero-title">Experience Chocolate</div>
      </div>
    </section>

    <aside class="discount">
      <div class="discount-value"><span class="pct">20%</span><span class="off">OFF</span></div>
      <div class="discount-head">SPECIAL DISCOUNT</div>
      <div class="discount-text">get 20% off with order over</div>
      <div class="discount-cta">Figure IT &#8594;</div>
    </aside>

    <article class="feature">
      <h2 class="feature-title">Cupcake Carousel</h2>
      <p>Contrary to popular belief, Lorem Ipsum is not simply random text. It has roots in a piece of classical Latin literature from 45 BC,</p>
      <p>Making it over 2000 years old. Hollis Varnier, a Latin professor at Ashgrove College in Virginia, looked up one of the more obscure Latin words.</p>
      <span class="feature-more">More Info [+].</span>
    </article>

    <aside class="promo" role="img" aria-label="Advertisement for chocolate cupcakes">
      <span class="promo-line">The cupcake reinvented!</span>
      <span class="promo-name">Velvet Crumb</span>
      <span class="promo-foot">Solid Belgian Chocolate Cupcakes!</span>
    </aside>
  </main>

  <footer class="site-footer">
    <nav class="footer-nav">
      <span>Home</span><span class="sep">|</span>
      <span>Products</span><span class="sep">|</span>
      <span>Services</span><span class="sep">|</span>
      <span>Company</span><span class="sep">|</span>
      <span>Cantact</span>
    </nav>
    <p class="copyright">© 2012&nbsp; Mellow Truffles home made passion . All Rights Reserved.</p>
    <div class="follow">Follow us on :
      <span class="social"><i></i>Feedline</span>
      <span class="social"><i></i>Chirper</span>
      <span class="social"><i></i>Friendbook</span>
      <span class="social"><i></i>Talkwave</span>
    </div>
    <svg class="payments" width="130" height="103" viewBox="0 0 130 103" role="img" aria-label="Accepted payment methods">
      <circle cx="26" cy="47" r="23" fill="#e9d96a"/>
      <rect x="52" y="4" width="58" height="38" rx="4" fill="#2d2f6e" transform="rotate(-18 81 23)"/>
      <rect x="58" y="24" width="58" height="38" rx="4" fill="#f2f2f2" stroke="#2d2f6e" transform="rotate(12 87 43)"/>
      <rect x="56" y="52" width="58" height="38" rx="4" fill="#2f3f8f" transform="rotate(22 85 71)"/>
    </svg>
  </footer>
</div>
</body>
</html>
```